Tarvimoor business cards

Need fresh design for our business cards. Logo must be specific, we are open for everything else.

Contact Information for Business Card

phrase "GMP & JANITORIAL SERVICES" should be used as main point of card

Colors
3176b5
3276b5
85acd3
cedeed
ffffff
0292cd
33a6d7
85cae6
cee9f5

Requirements
Must have
• The logo
Should not have
• crowded designs

```html
<!DOCTYPE html>
<html lang="en">
<head>
<meta charset="utf-8">
<title>Tarvimoor business cards</title>
<link href="https://fonts.googleapis.com/css2?family=Open+Sans:wght@400;600&display=swap" rel="stylesheet">
<style>
  :root {
    --brand-blue: #1a80c4;
    --ink: #2a2a2a;
    --paper: #ffffff;
    --stage: #3a3a3c;
    --stripe-dark: #111111;
  }
  * { margin: 0; padding: 0; box-sizing: border-box; }
  html, body {
    width: 1200px; height: 900px; overflow: hidden;
    background: var(--stage);
    font-family: "Open Sans", Arial, sans-serif;
  }
  .card-sheet { position: relative; width: 1200px; height: 900px; }
  .card {
    position: absolute; left: 250px; width: 700px; height: 400px;
    border-radius: 28px; overflow: hidden;
  }
  .card-front { top: 30px; background: var(--brand-blue); color: var(--paper); }
  .card-back { top: 470px; background: var(--paper); color: var(--ink); }

  .brand-lockup { position: absolute; display: flex; flex-direction: column; align-items: flex-end; }
  .brand-mark {
    display: flex; align-items: center; gap: 14px;
    font-weight: 400; letter-spacing: 0.2em; text-transform: uppercase; line-height: 1;
  }
  .brand-mark .brand-dot { width: 14px; height: 14px; border-radius: 50%; background: currentColor; }
  .brand-tagline {
    font-weight: 600; text-transform: uppercase; letter-spacing: 0.28em; white-space: nowrap;
  }

  .card-front .brand-lockup { left: 50%; top: 130px; transform: translateX(-50%); }
  .card-front .brand-mark { font-size: 52px; }
  .card-front .brand-tagline { font-size: 15px; margin-top: 14px; }
  .card-front .front-web {
    position: absolute; left: 0; right: 0; top: 300px;
    text-align: center; font-size: 19px;
  }

  .card-back .brand-lockup { right: 46px; top: 52px; color: var(--brand-blue); }
  .card-back .brand-mark { font-size: 34px; gap: 10px; }
  .card-back .brand-mark .brand-dot { width: 10px; height: 10px; }
  .card-back .brand-tagline { font-size: 10.5px; margin-top: 9px; }

  .contact-block { position: absolute; left: 58px; top: 54px; }
  .contact-name { font-size: 27px; font-weight: 600; color: var(--brand-blue); line-height: 1.1; }
  .contact-title { font-size: 16px; margin-bottom: 12px; }
  .contact-list { list-style: none; font-size: 16px; line-height: 1.55; }
  .contact-list .label { color: var(--brand-blue); }

  .divider {
    position: absolute; left: 250px; right: 54px; top: 150px;
    height: 1px; background: var(--brand-blue);
  }
  .address {
    position: absolute; right: 56px; top: 250px;
    font-size: 18px; line-height: 1.4; font-style: normal;
  }
  .bottom-wave { position: absolute; left: 0; bottom: 0; width: 700px; height: 400px; }
</style>
</head>
<body>
<main class="card-sheet">
  <section class="card card-front" aria-label="Card front">
    <div class="brand-lockup">
      <div class="brand-mark"><span>Tarvimoor</span><span class="brand-dot"></span></div>
      <p class="brand-tagline">GMP &amp; Janitorial Services</p>
    </div>
    <p class="front-web">www.tarvimoorclean.com</p>
  </section>

  <section class="card card-back" aria-label="Card back">
    <svg class="bottom-wave" viewBox="0 0 700 400" aria-hidden="true">
      <path d="M0 232 C 120 290, 260 320, 420 334 C 540 344, 640 350, 700 360"
            fill="none" stroke="var(--brand-blue)" stroke-width="3"/>
      <path d="M0 252 C 130 310, 280 338, 440 348 C 560 356, 650 364, 700 374"
            fill="none" stroke="var(--stripe-dark)" stroke-width="5"/>
      <path d="M0 262 C 130 320, 280 348, 440 358 C 560 366, 650 374, 700 384 L700 400 L0 400 Z"
            fill="var(--brand-blue)"/>
    </svg>

    <div class="contact-block">
      <h1 class="contact-name">Elena Varsk</h1>
      <p class="contact-title">General Manager</p>
      <ul class="contact-list">
        <li><span class="label">P:</span> 5550148213</li>
        <li><span class="label">M:</span> 5550172964(office)</li>
        <li><span class="label">E:</span> hello@tarvimoorclean.com</li>
        <li><span class="label">W:</span> www.tarvimoorclean.com</li>
      </ul>
    </div>

    <div class="brand-lockup">
      <div class="brand-mark"><span>Tarvimoor</span><span class="brand-dot"></span></div>
      <p class="brand-tagline">GMP &amp; Janitorial Services</p>
    </div>
    <div class="divider"></div>

    <address class="address">
      Alder Crossing<br>
      Wrenfield Heights, 4820
    </address>
  </section>
</main>
</body>
</html>
```